Etikett für einen Rosé Wein
Zielgruppe
Wir sind ein Weingut und benötigen ein neues Etikett für unseren Muskattrollinger Rosé. Unsere Kunden sind eher traditionelle Weinkäufer.
Aufgabenstellung
Format:
Höhe: 9 cm
Breite: 11 cm
Da es nur ein Vorderetikett gibt, müssen alle relevanten Angaben (Hersteller, Alkohol, Inhalt in L, Rebsorte, etc.) enthalten sein. (siehe Flaschenabbildung anbei)
WÜRTTEMBERG
2019er
Muskattrollinger Rosé
DEUTSCHER QUALITÄTSWEIN
11,0 % Vol.
0,75 l
Enthält Sulfite
A.P.Nr. 58271346
Abfüller
Straße / PLZ / Ort / Tel.
Der Flaschenverschluss ist schwarz d.h. das neue Etikettendesign sollte dazu passen.
Bisher ist der Hintergrund des Weinetiketts schwarz. Dies muss jedoch nicht so bleiben.
Im Anhang finden Sie außerdem ein Plakat. Ggf. können Sie für das Flaschendesign einige nostalgische Elemente davon übernehmen.

```html
<!DOCTYPE html>
<html lang="de">
<head>
<meta charset="utf-8">
<title>Muskattrollinger Rosé – Etikett</title>
<link rel="stylesheet" href="https://fonts.googleapis.com/css2?family=Grenze+Gotisch:wght@500;600&family=Merriweather:wght@400;700&display=swap">
<style>
  :root {
    --page: #ffffff;
    --label: #ab8996;
    --ink: #ffffff;
    --ornament: rgba(255,255,255,0.55);
  }
  * { margin: 0; padding: 0; box-sizing: border-box; }
  html, body { width: 667px; height: 1200px; overflow: hidden; background: var(--page); }
  .label {
    position: absolute;
    left: 33px; top: 355px;
    width: 600px; height: 489px;
    background: var(--label);
    color: var(--ink);
    font-family: "Merriweather", Georgia, serif;
  }
  .frame { position: absolute; inset: 0; }
  .text { position: absolute; white-space: nowrap; line-height: 1; }
  .gothic { font-family: "Grenze Gotisch", "Times New Roman", serif; font-weight: 600; }
  .volume { left: 35px; top: 40px; font-size: 25px; line-height: 27px; }
  .vintage { right: 38px; top: 40px; font-size: 25px; }
  .region { left: 0; width: 600px; text-align: center; top: 158px; font-size: 21px; letter-spacing: 0.5px; }
  .variety { left: 0; width: 600px; text-align: center; top: 205px; font-size: 70px; line-height: 54px; }
  .sulfite { left: 34px; top: 352px; font-size: 16px; letter-spacing: 0.3px; }
  .ap-number { right: 38px; top: 352px; font-size: 16px; letter-spacing: 0.3px; }
  .bottler { left: 0; width: 600px; text-align: center; top: 390px; font-size: 21px; line-height: 31px; font-weight: 700; letter-spacing: 0.8px; }
  .ornament { position: absolute; background: var(--ornament); border-radius: 14px; }
  .ornament-top { left: 157px; top: 14px; width: 285px; height: 26px; }
  .ornament-bottom { left: 157px; top: 455px; width: 285px; height: 26px; }
  .grapes { position: absolute; left: 231px; top: 91px; width: 143px; height: 55px; background: radial-gradient(ellipse at 40% 50%, rgba(255,255,255,0.7), rgba(255,255,255,0.25)); border-radius: 28px; }
  .arc { position: absolute; left: 0; top: 0; }
</style>
</head>
<body>
  <div class="label">
    <svg class="frame" width="600" height="489" viewBox="0 0 600 489" aria-hidden="true">
      <g fill="none" stroke="#ffffff" stroke-width="2">
        <polyline points="143,20 23,20 23,471 143,471"/>
        <polyline points="456,20 575,20 575,471 456,471"/>
      </g>
    </svg>
    <div class="ornament ornament-top" role="img" aria-label="Verschnörkelte Zierranke"></div>
    <div class="ornament ornament-bottom" role="img" aria-label="Verschnörkelte Zierranke"></div>

    <div class="text volume gothic">11,0 % Vol.<br>0,75 l</div>
    <div class="text vintage gothic">2019er</div>

    <svg class="arc" width="600" height="200" viewBox="0 0 600 200" aria-label="DEUTSCHER QUALITÄTSWEIN">
      <defs><path id="arc-path" d="M150,112 Q300,30 450,112"/></defs>
      <text font-family="Merriweather, Georgia, serif" font-size="16.5" fill="#ffffff" letter-spacing="0.6">
        <textPath href="#arc-path" startOffset="50%" text-anchor="middle">DEUTSCHER QUALITÄTSWEIN</textPath>
      </text>
    </svg>
    <div class="grapes" role="img" aria-label="Zeichnung einer Weintraube mit Blatt"></div>

    <div class="text region">WÜRTTEMBERG</div>
    <div class="text variety gothic">Muskattrollinger<br>Rosé</div>

    <div class="text sulfite">Enthält Sulfite</div>
    <div class="text ap-number">A.P. Nr.58271346</div>

    <div class="text bottler">Abfüller<br>Straße &nbsp;/&nbsp; PLZ &nbsp;/&nbsp; Ort &nbsp;/&nbsp; Tel.</div>
  </div>
</body>
</html>
```